Alaska Law Firm Needs a Sticker Design

We need a design for stickers to put on already-printed brochures. We mail the brochures to potential clients so they can learn more about accident-induced injuries, insurance claims, legal representation, and our own law firm.

One of our lawyers wrote a book that provides a helpful overview of personal injury claims. We are offering this book for free to anyone who calls and requests it. Therefore, the sticker design should include one of the following phrases, or something very similar:
a) "Still have questions? Call and request our book-- for free!"
b) "Still have questions about auto accident claims? Call and request our book today."
c) "Still have questions about filing a claim? Call and request a free copy of our book."
d) "Still have questions? Call us today to request a free copy of our book, Clear Lanes Ahead."
e) "To learn more about automobile accidents and insurance, call today and request a free copy of our book."

The sticker should be approximately 3"x3" and may be a circle, square, rectangle, or ellipsis. The sticker will be placed on the back of the folder, which is light blue. We would like the sticker to match the color scheme of our website and the folder.

I will upload an image of the book cover as soon as I obtain it.

Industry/Entity Type

Law Firm

Font styles to use
Serif
Sans Serif

Requirements
Should not have
• Bright colors that aren't already used in the folder design. e.g. no bright orange, pink, chartreuse, turquoise, yellow, red.

```html
<!DOCTYPE html>
<html lang="en">
<head>
<meta charset="utf-8">
<title>Free Book Sticker – Whitcomb Law Group</title>
<link rel="stylesheet" href="https://fonts.googleapis.com/css2?family=Cinzel:wght@400;500&family=EB+Garamond:ital,wght@1,400&family=Open+Sans:wght@300;400;600;700;800&display=swap">
<style>
  :root {
    --navy: #143f6b;
    --ink-navy: #14164a;
    --sky: #d6e4f5;
    --white: #ffffff;
    --body-ink: #222222;
    --accent-red: #c0272d;
    --photo-sky: #dfe8e6;
    --photo-grass: #7fae4a;
  }
  * { box-sizing: border-box; margin: 0; padding: 0; }
  html, body { width: 1200px; height: 1200px; overflow: hidden; }
  body { position: relative; background: var(--sky); font-family: "Open Sans", sans-serif; }

  .headline-band {
    position: absolute; left: 0; top: 0; width: 1200px; height: 453px;
    background: var(--navy); color: var(--white);
    font-family: "Cinzel", serif; text-align: center;
  }
  .headline-band .line { position: absolute; left: 0; width: 100%; white-space: nowrap; }
  .line-1 { top: 38px; font-size: 66px; }
  .line-2 { top: 130px; font-size: 66px; }
  .line-3 { top: 222px; font-size: 66px; }
  .line-4 { top: 313px; font-size: 128px; letter-spacing: 4px; line-height: 1; }

  .book {
    position: absolute; left: 314px; top: 500px; width: 578px; height: 444px;
    border: 1.5px solid #2a2a2a; background: var(--white); overflow: hidden;
  }
  .book-footer { position: absolute; left: 0; bottom: 0; width: 100%; height: 51px; background: var(--ink-navy); }

  .back-cover { position: absolute; left: 0; top: 0; width: 282px; height: 393px; padding: 18px 14px 0 26px; color: var(--body-ink); font-size: 6.4px; line-height: 1.3; }
  .back-cover p { margin-bottom: 6px; text-align: justify; }
  .back-cover .teaser { color: var(--accent-red); text-align: center; text-transform: uppercase; font-weight: 600; margin-bottom: 6px; }
  .back-cover .rule { width: 220px; height: 1px; background: var(--accent-red); margin: 10px auto 12px; }
  .bio-row { display: flex; gap: 8px; }
  .author-photo { flex: 0 0 69px; height: 86px; background: linear-gradient(160deg, #7f93ab, #2c3f73); }
  .bio-row .bio-text { flex: 1; }
  .brand-mark { position: absolute; left: 26px; top: 352px; display: flex; align-items: center; gap: 6px; color: var(--ink-navy); font-family: "Cinzel", serif; font-size: 12px; line-height: 1.1; }
  .brand-mark .square { width: 26px; height: 26px; background: var(--ink-navy); }

  .spine { position: absolute; left: 282px; top: 0; width: 11px; height: 100%; background: var(--ink-navy); }
  .spine-text { position: absolute; left: 283px; top: 160px; width: 10px; writing-mode: vertical-rl; color: var(--ink-navy); font-size: 7px; font-weight: 700; white-space: nowrap; }
  .spine-text .author { font-weight: 400; margin-top: 18px; }
  .spine-strip { position: absolute; left: 293px; top: 0; width: 10px; height: 393px; background: var(--white); }

  .front-cover { position: absolute; left: 293px; top: 0; width: 285px; height: 393px; text-align: center; color: var(--ink-navy); }
  .front-cover .author-name { margin-top: 16px; font-weight: 300; font-size: 19px; letter-spacing: -0.8px; }
  .front-cover .title { margin-top: 4px; font-weight: 800; font-size: 37px; line-height: 0.98; letter-spacing: -1.5px; text-transform: uppercase; }
  .cover-photo { position: absolute; left: 3px; top: 118px; width: 282px; height: 275px; background: linear-gradient(180deg, var(--photo-sky) 0%, #c9d8b8 45%, var(--photo-grass) 100%); }
  .front-subtitle { position: absolute; left: 293px; bottom: 0; width: 285px; height: 51px; padding-top: 7px; color: var(--white); text-align: center; font-size: 13.5px; line-height: 1.25; font-weight: 600; text-transform: uppercase; }

  .phone-band { position: absolute; left: 0; top: 1002px; width: 1200px; height: 93px; background: var(--navy); color: var(--white); text-align: center; font-family: "EB Garamond", serif; font-style: italic; font-size: 58px; line-height: 93px; letter-spacing: 1px; }
  .tagline { position: absolute; left: 0; top: 1108px; width: 1200px; text-align: center; color: var(--navy); font-family: "EB Garamond", serif; font-style: italic; font-size: 58px; letter-spacing: 0.5px; }
</style>
</head>
<body>
  <header class="headline-band">
    <div class="line line-1">Still have questions?</div>
    <div class="line line-2">Call and request</div>
    <div class="line line-3">our book</div>
    <div class="line line-4">FOR FREE</div>
  </header>

  <figure class="book" aria-label="Book cover: Clear Lanes Ahead">
    <div class="book-footer"></div>

    <div class="back-cover">
      <p class="teaser">Most drivers will face a road accident at least once in their lives, and many will face two or three.</p>
      <p>If you have avoided a crash so far, count yourself fortunate. It still pays to be ready, so you know the right steps when it happens.</p>
      <p>If you were recently in a crash and feel unsure, these pages explain what comes next. Written for Alaska drivers, this guide covers your rights and the steps to take after a collision.</p>
      <div class="rule"></div>
      <div class="bio-row">
        <div class="author-photo" role="img" aria-label="Portrait photo of the author"></div>
        <div class="bio-text">
          <p>A science graduate before law school, Daniel chose the courtroom over a career in medicine and brought that training into his practice.</p>
          <p>His first legal post was with a defense firm handling medical claims. He soon learned that defending insurers did not suit someone who stood for the injured person.</p>
        </div>
      </div>
      <p>Committed to helping people rather than insurers, Daniel opened his own plaintiff firm, where he helped thousands receive fair pay for their injuries.</p>
      <p>He later moved north and founded Whitcomb Law Group, and since then hundreds of Alaskans have turned to the firm for help.</p>
      <p>Most cases settle out of court, yet two decades of practice show that insurers pay fairly when they know a trial is a real option.</p>
    </div>
    <div class="brand-mark"><span class="square"></span><span>WHITCOMB<br>LAW GROUP</span></div>

    <div class="spine"></div>
    <div class="spine-strip"></div>
    <div class="spine-text">CLEAR LANES AHEAD<span class="author">DANIEL R. WHITCOMB</span></div>

    <div class="front-cover">
      <div class="author-name">DANIEL R. WHITCOMB</div>
      <div class="title">Clear Lanes<br>Ahead</div>
      <div class="cover-photo" role="img" aria-label="Photo of a smiling family lying on a lawn beside a small red car"></div>
    </div>
    <div class="front-subtitle">The right way to handle<br>your auto accident claim</div>
  </figure>

  <div class="phone-band">(907) 555- 0148</div>
  <p class="tagline">We’ll help you get back what you love</p>
</body>
</html>
```